Boat wrap for boat graphics company (Ironic, I know)

We are a boat graphics company, but have a very hard time designing something for ourselves. I would like to refresh our boat wrap. The logo, KV & Plura logos stay as they are. The original (attached) is a simple background from Pixorva.com (#48193726), which I have stretched to give the effect I was looking for. I'm not looking for one of these super colorful / shocking design. Just want something like what I have now, but new. Something flowing, that shows movement (movement, but not necessarily speed). Dark shades of blue are a must, so logo can pop.

Target Market(s)

Boat owners

Industry/Entity Type

Boat / Yacht

Colors
0054AA
0677BA
7BADD7
CADEEF
E8F1F8

Requirements
Must have
• Color Blue
Nice to have
• Not against a marlin texture background, as long as it doesnt interfere with the logo. The Harbor Skiffs Collective boats usually look very cool. These are designed by Vintu
Should not have
• Too many colors

```html
<!DOCTYPE html>
<html lang="en">
<head>
<meta charset="utf-8">
<title>HullWrapStudio Boat Wrap Banner</title>
<link rel="stylesheet" href="https://fonts.googleapis.com/css2?family=Exo+2:wght@700&display=swap">
<style>
  :root {
    --page-white: #ffffff;
    --navy-deep: #03084a;
    --navy-mid: #081467;
    --wave-blue: #0c2a9a;
    --wave-glow: #1a3fc0;
    --badge-blue: #1f4fc8;
    --text-white: #ffffff;
  }
  html, body {
    margin: 0;
    padding: 0;
    width: 1200px;
    height: 180px;
    overflow: hidden;
    background: var(--page-white);
  }
  .wrap-banner {
    position: absolute;
    left: 11px;
    top: 11px;
    width: 1178px;
    height: 158px;
    background: var(--navy-deep);
    overflow: hidden;
  }
  .wrap-banner__backdrop {
    position: absolute;
    inset: 0;
    width: 100%;
    height: 100%;
  }
  .brand-line {
    position: absolute;
    left: 129px;
    top: 64px;
    height: 52px;
    display: flex;
    align-items: center;
    gap: 14px;
  }
  .social-badge {
    width: 50px;
    height: 50px;
    border-radius: 5px;
    background: var(--badge-blue);
    display: flex;
    align-items: center;
    justify-content: center;
    font-family: "Exo 2", sans-serif;
    font-weight: 700;
    font-size: 20px;
    color: var(--text-white);
  }
  .web-address {
    font-family: "Exo 2", sans-serif;
    font-weight: 700;
    font-size: 62px;
    line-height: 1;
    letter-spacing: 1px;
    color: var(--text-white);
    white-space: nowrap;
  }
</style>
</head>
<body>
  <div class="wrap-banner">
    <svg class="wrap-banner__backdrop" viewBox="0 0 1178 158" preserveAspectRatio="none">
      <defs>
        <linearGradient id="backdropShade" x1="0" y1="0" x2="0" y2="1">
          <stop offset="0" stop-color="#03084a"/>
          <stop offset="1" stop-color="#081467"/>
        </linearGradient>
        <linearGradient id="waveShade" x1="0" y1="0" x2="1" y2="0">
          <stop offset="0" stop-color="#0c2a9a"/>
          <stop offset="0.5" stop-color="#081467"/>
          <stop offset="1" stop-color="#1a3fc0"/>
        </linearGradient>
      </defs>
      <rect class="texture-field" role="img" aria-label="Faint hexagon texture across the dark navy field" x="0" y="0" width="1178" height="158" fill="url(#backdropShade)"/>
      <path class="flow-wave" d="M0 128 C 200 110, 420 112, 640 128 C 860 144, 1050 120, 1178 78 L1178 158 L0 158 Z" fill="url(#waveShade)" opacity="0.85"/>
      <path class="flow-wave-crest" d="M0 128 C 200 110, 420 112, 640 128 C 860 144, 1050 120, 1178 78" fill="none" stroke="#1a3fc0" stroke-width="1.5" opacity="0.6"/>
    </svg>
    <div class="brand-line">
      <div class="social-badge">KV</div>
      <div class="web-address">HULLWRAPSTUDIO.COM</div>
    </div>
  </div>
</body>
</html>
```